Emergency Management Consulting Needs a Website

Need to develop a website for an Emergency Management Consulting business. This website needs to be user friendly and resemble disaster preparedness, response, recovery, and mitigation. It must allow for me to make changes to it myself by adding pages, content and pictures. Looking for an advanced page to the website that allows monitoring of social media sites, hashtags, and keywords. Must have pictures of disasters on the site. Must try to integrate the logo colors, not excessive.

Reason: Did not receive anything sufficient to what I am looking for.

Industry/Entity Type

Government

Coding

Coded - Design and coding required

Number of Pages Required

5+ page

Requirements
Must have
• Logo, advanced social media monitoring page, allow for edits myself (content, pages, graphics) this must be a CMS of some sort, use logo color scheme (not excessively), must be professional looking, connect with Pexaro Domain, find a hosting site, SEO, no "long" designs, minimize "dead" space, no social media feeds, no newsletter stuff.
• Menu items: Home, About Us, Services, Situation Monitor, Work With Us, Contact Us (hopefully these could be editable if I need to later)
• When you make a submission, please send me a message on which CMS you are using. Thank you.
Nice to have
• Examples of websites:
• https://www.qarl.vic.gov.au/
• http://www.malvecorish.com/
• http://www.tuvrakol.org/
• http://pomvaleconsulting.com/
• http://www.sultavon.com/services/emergency-management
• https://uzo.com/
• http://www.velumbra.com/Responsibility/Sustainable-Development/HSE/Crisis-and-Emergency-Management/

```html
<!DOCTYPE html>
<html lang="en">
<head>
<meta charset="utf-8">
<title>Kestrel Ridge Emergency Management</title>
<link href="https://fonts.googleapis.com/css2?family=Source+Sans+3:wght@400;600;700&display=swap" rel="stylesheet">
<style>
:root{
  --ink:#333;
  --muted:#555;
  --red:#e2352b;
  --blue:#1e9ad6;
  --navy:#1f3f8f;
  --yellow:#f2c30f;
  --gray-bg:#efefef;
  --band:#6b6b6b;
  --panel:rgba(60,130,190,.85);
}
*{box-sizing:border-box;margin:0;padding:0}
html,body{width:748px;height:1200px;overflow:hidden;background:#fff}
body{position:relative;font-family:"Source Sans 3",sans-serif;color:var(--ink)}
.abs{position:absolute}
.topline{left:0;top:0;width:748px;height:2px;background:linear-gradient(90deg,var(--navy),var(--blue),var(--red),var(--yellow))}
.brand{left:58px;top:14px;display:flex;align-items:center;gap:7px}
.brand-dot{width:26px;height:26px;border-radius:50%;background:var(--blue)}
.brand-name{font-size:17px;font-weight:700;color:var(--ink);letter-spacing:.5px;line-height:1}
.search{left:557px;top:12px;width:132px;height:18px;border:1px solid #ddd;border-radius:9px}
.search svg{position:absolute;right:6px;top:3px}
.nav{right:59px;top:36px;display:flex;font-size:8px;color:#666}
.nav a{color:inherit;text-decoration:none;padding:0 8px;line-height:20px}
.nav a.active{border:1px solid #ddd;border-bottom:none;background:#fff;color:var(--ink);padding:0 12px}
.hero{left:0;top:58px;width:748px;height:348px;background:linear-gradient(120deg,#7a5a3c,#b8875a 45%,#d7b08a 65%,#6d4a30)}
.hero-panel{left:58px;top:188px;width:249px;height:127px;background:var(--panel);padding:10px 13px;color:#fff}
.hero-panel h1{font-size:19px;line-height:22px;font-weight:400}
.hero-panel h1 b{font-weight:700}
.hero-panel .rule{width:26px;height:2px;background:#fff;margin:8px 0 7px}
.hero-panel p{font-size:7.2px;line-height:9.5px}
.btn{left:73px;top:306px;width:74px;height:17px;border-radius:9px;background:#fff;color:var(--ink);font-size:7.5px;text-align:center;line-height:17px}
.dots{left:358px;top:386px;display:flex;gap:6px}
.dots i{width:6px;height:6px;border-radius:50%;background:#fff}
.dots i:first-child{background:var(--yellow)}
.welcome{left:0;top:406px;width:748px;text-align:center}
.welcome .kicker{margin-top:24px;font-size:9px}
.welcome h2{font-size:15px;font-weight:400;color:var(--red);margin-top:2px}
.welcome .bar{width:26px;height:2px;background:var(--red);margin:6px auto 7px}
.welcome p{font-size:7.5px;line-height:9.5px;color:var(--muted)}
.services{left:0;top:516px;width:748px;height:416px;background:var(--gray-bg)}
.notch{left:366px;top:516px;width:0;height:0;border-left:8px solid transparent;border-right:8px solid transparent;border-top:9px solid #fff}
.tile{overflow:hidden}
.tile .photo{width:100%;height:100%}
.cap{position:absolute;left:0;bottom:0;right:0;height:53px;background:rgba(40,40,40,.55);color:#fff;padding:6px 40px 0 6px}
.cap.light{background:rgba(245,245,245,.8);color:var(--ink)}
.cap.red{background:rgba(226,53,43,.9)}
.cap h3{font-size:10px;font-weight:600;line-height:12px}
.cap p{font-size:7px;line-height:8.5px}
.tile.wide .cap{height:40px;padding-top:17px}
.corner{position:absolute;right:0;bottom:0}
.play{position:absolute;left:81px;top:70px}
.footer-col{top:956px;font-size:7.3px;line-height:12.4px;color:#444}
.footer-col h4{font-size:10px;font-weight:600;color:var(--ink);line-height:14px}
.footer-col .u{width:26px;height:2px;margin:4px 0 8px}
.subscribe{left:542px;top:986px;display:flex}
.subscribe .field{width:108px;height:17px;border:1px solid #ddd;font-size:6.5px;color:#aaa;padding:0 6px;line-height:15px;background:#fff}
.subscribe .send{width:24px;height:17px;background:var(--yellow);display:flex;align-items:center;justify-content:center}
.social{left:543px;top:1016px;display:flex;gap:8px}
.social i{width:15px;height:15px;border-radius:50%;background:#ddd}
.social i:first-child{background:var(--yellow)}
.skyline{left:0;top:1068px;width:748px;height:38px;background:linear-gradient(180deg,#fff,#cfe3c8 60%,#9bc48a)}
.contact{left:0;top:1106px;width:748px;height:68px;background:var(--band);color:#fff}
.contact .cell{position:absolute;top:0;height:68px;display:flex;align-items:center;gap:12px;font-size:10px;line-height:12.5px}
.contact .div{position:absolute;top:0;width:1px;height:68px;background:#888}
.circle{width:36px;height:36px;border-radius:50%;background:#fff;display:flex;align-items:center;justify-content:center;flex:none}
.bottombar{left:0;top:1174px;width:748px;height:26px;background:var(--blue);color:#fff;font-size:7.5px}
.bottombar nav{position:absolute;left:58px;top:8px;display:flex;gap:9px}
.bottombar nav a{color:#fff;text-decoration:none}
.bottombar nav a:first-child{color:var(--yellow)}
.bottombar .copy{position:absolute;right:59px;top:9px;font-size:7px}
</style>
</head>
<body>
<div class="abs topline"></div>

<header>
  <div class="abs brand"><span class="brand-dot"></span><span class="brand-name">KESTREL RIDGE</span></div>
  <div class="abs search"><svg width="10" height="10" viewBox="0 0 10 10"><circle cx="4" cy="4" r="3" fill="none" stroke="#999" stroke-width="1.2"/><line x1="6.2" y1="6.2" x2="9" y2="9" stroke="#999" stroke-width="1.4"/></svg></div>
  <nav class="abs nav">
    <a class="active" href="#">Home</a><a href="#">About Us</a><a href="#">Services</a><a href="#">Situation Monitor</a><a href="#">Work With Us</a><a href="#">Contact Us</a>
  </nav>
</header>

<section class="abs hero" role="img" aria-label="Rescue crew in helmets carrying a ladder through smoke"></section>
<div class="abs hero-panel">
  <h1><b>Disaster Recovery</b> Doesn't Have To Be <b>Intimidating</b></h1>
  <div class="rule"></div>
  <p>With KESTREL RIDGE's team of experienced professionals, you can recover quickly and compliantly, with full confidence that you are doing everything right.</p>
</div>
<div class="abs btn">Read More</div>
<div class="abs dots"><i></i><i></i><i></i></div>

<section class="abs welcome">
  <div class="kicker">Welcome to a Kestrel Ridge</div>
  <h2>Safe. Secure. Resilient.</h2>
  <div class="bar"></div>
  <p>We are Global Leader in emergancy managment. We integrate science, technology, and real-world<br>experience to provide each of our customers with solutions</p>
</section>

<section class="abs services"></section>
<div class="abs notch"></div>

<article class="abs tile" style="left:58px;top:536px;width:202px;height:178px">
  <div class="photo" role="img" aria-label="Dark response van parked outside a house" style="background:linear-gradient(160deg,#6f7580,#2c2f36 60%,#1b1d22)"></div>
  <svg class="play" width="40" height="40" viewBox="0 0 40 40"><circle cx="20" cy="20" r="17" fill="rgba(0,0,0,.25)" stroke="#fff" stroke-width="2"/><path d="M15 12 L28 20 L15 28 Z" fill="none" stroke="#fff" stroke-width="2" stroke-linejoin="round"/></svg>
</article>

<article class="abs tile wide" style="left:272px;top:536px;width:417px;height:178px">
  <div class="photo" role="img" aria-label="Aid workers in red jackets tending a person wrapped in a foil blanket" style="background:linear-gradient(120deg,#c9443a,#d85a4f 40%,#b9b1a6 75%,#8d8880)"></div>
  <div class="cap light"><h3>Disaster preparedness</h3><p>Lorem ipsum dolor sit amet, consectetur adipiscing elit. Nulla cursus at arcu eu mollis nam sit amet magna eget.</p></div>
  <svg class="corner" width="40" height="32" viewBox="0 0 40 32"><path d="M40 0 V32 H0 Z" fill="var(--yellow)"/><path d="M27 16 L32 21 L27 26" fill="none" stroke="#fff" stroke-width="2"/></svg>
</article>

<article class="abs tile" style="left:58px;top:726px;width:202px;height:178px">
  <div class="photo" role="img" aria-label="Workers in hard hats and safety vests on a rubble site" style="background:linear-gradient(150deg,#cbb79a,#b9a23f 45%,#8a7a66)"></div>
  <div class="cap light"><h3>Quick response</h3><p>Lorem ipsum dolor sit amet, consectetur adipiscing elit. Nulla cursus at arcu eu mollis.</p></div>
  <svg class="corner" width="40" height="32" viewBox="0 0 40 32"><path d="M40 0 V32 H0 Z" fill="var(--yellow)"/><path d="M27 16 L32 21 L27 26" fill="none" stroke="#fff" stroke-width="2"/></svg>
</article>

<article class="abs tile" style="left:272px;top:726px;width:202px;height:178px">
  <div class="photo" role="img" aria-label="Rescuer in a red helmet supporting an injured person" style="background:linear-gradient(150deg,#9a3a33,#c9584c 50%,#6b4a44)"></div>
  <div class="cap red"><h3>Best way to recover</h3><p>Lorem ipsum dolor sit amet, consectetur adipiscing</p></div>
  <svg class="corner" width="40" height="32" viewBox="0 0 40 32"><path d="M40 0 V32 H0 Z" fill="#333"/><path d="M27 16 L32 21 L27 26" fill="none" stroke="#fff" stroke-width="2"/></svg>
</article>

<article class="abs tile" style="left:487px;top:726px;width:202px;height:178px">
  <div class="photo" role="img" aria-label="Hands holding a paper sign reading disaster recovery plan" style="background:linear-gradient(160deg,#3a3a3e,#6e6e72 50%,#2a2a2d)"></div>
  <div class="cap"><h3>Mitigation strategies</h3><p>Lorem ipsum dolor sit amet, consectetur adipiscing elit. Nulla cursus at arcu.</p></div>
  <svg class="corner" width="40" height="32" viewBox="0 0 40 32"><path d="M40 0 V32 H0 Z" fill="var(--yellow)"/><path d="M27 16 L32 21 L27 26" fill="none" stroke="#fff" stroke-width="2"/></svg>
</article>

<footer>
  <div class="abs footer-col" style="left:58px;top:948px">
    <div class="brand" style="position:static"><span class="brand-dot" style="width:20px;height:20px"></span><span class="brand-name" style="font-size:13px">KESTREL RIDGE</span></div>
    <div class="u" style="background:var(--blue);margin-top:6px"></div>
    <div>Marlow Falls, IL<br>2740 Halbrook Avenue , Suite 201<br>Marlow Falls, IL 60999</div>
    <div style="margin-top:6px">Fenwick, DC<br>4812 Larch Street NW, Suite 600<br>Fenwick, DC 20999</div>
  </div>
  <div class="abs footer-col" style="left:225px">
    <h4>About Us</h4><div class="u" style="background:var(--navy)"></div>
    Emergency Management Commissioner<br>Chief Executive<br>Our Vision, Goals and Values<br>Our structure<br>Working as one
  </div>
  <div class="abs footer-col" style="left:396px">
    <h4>Find</h4><div class="u" style="background:var(--red)"></div>
    Careers<br>Grants<br>Incident management<br>Strategic Action Plan<br>Emergency Management Manual
  </div>
  <div class="abs footer-col" style="left:542px">
    <h4>Stay with Us</h4><div class="u" style="background:var(--yellow)"></div>
  </div>
  <div class="abs subscribe"><div class="field">Enter your email Id</div><div class="send"><svg width="12" height="10" viewBox="0 0 12 10"><path d="M1 5 L11 1 L8 9 L6 6 Z" fill="#fff"/></svg></div></div>
  <div class="abs social"><i></i><i></i><i></i><i></i></div>

  <div class="abs skyline" role="img" aria-label="Colourful illustrated city skyline with trees and a ferris wheel"></div>

  <div class="abs contact">
    <div class="cell" style="left:122px"><span class="circle"><svg width="18" height="18" viewBox="0 0 24 24"><path d="M6.6 10.8a15 15 0 0 0 6.6 6.6l2.2-2.2c.3-.3.7-.4 1-.2 1.1.4 2.3.6 3.6.6.6 0 1 .4 1 1V20c0 .6-.4 1-1 1A17 17 0 0 1 3 4c0-.6.4-1 1-1h3.5c.6 0 1 .4 1 1 0 1.3.2 2.5.6 3.6.1.3 0 .7-.2 1z" fill="var(--band)"/></svg></span><span>Call Us at<br>(055) 555-0142 /<br>+9055510387</span></div>
    <div class="div" style="left:276px"></div>
    <div class="cell" style="left:301px"><span class="circle"><svg width="16" height="18" viewBox="0 0 16 20"><path d="M8 1a6 6 0 0 0-6 6c0 4.5 6 12 6 12s6-7.5 6-12a6 6 0 0 0-6-6z" fill="var(--band)"/><circle cx="8" cy="7" r="2.3" fill="#fff"/></svg></span><span>Find Where<br>We Are</span></div>
    <div class="div" style="left:443px"></div>
    <div class="cell" style="left:467px"><span class="circle"><svg width="18" height="14" viewBox="0 0 18 14"><rect x="1" y="1" width="16" height="12" rx="1.5" fill="var(--band)"/><path d="M1.5 2 L9 8 L16.5 2" fill="none" stroke="#fff" stroke-width="1.4"/></svg></span><span>Write To Us For<br>Queries &amp; Feedback</span></div>
  </div>

  <div class="abs bottombar">
    <nav><a href="#">Home</a><a href="#">About Us</a><a href="#">Services</a><a href="#">Situation Monitor</a><a href="#">Work With Us</a><a href="#">Contact Us</a></nav>
    <div class="copy">Copyright © 2017 Kestrel Ridge. All rights reserved.</div>
  </div>
</footer>
</body>
</html>
```